Horizzontal format 2 m long x 0,80 m high

We need a horizzontal format design for a rectangular board 2m long and 0,8 meter high.

The board will be positioned on a side of soccer fields, so the text should be readable for the other side of the field.
Color:text colors should be read, and grey.

Copy:
"Murastella Impresa Edile.
Pensiamo a TUTTO NOI, dall'ideazione alla REALIZZAZIONE

Ristrutturazioni d'Interni ed Esterni,
Progettazione con la collaborazione di un TEAM DI ARCHITETTI E INGEGNERI
Realizzazione con materiali di altissimo livello (only if there is enough space!)
CURA DEI particolari per ottenere grandi risultati (only if there is enough space!)

TOTAL RELAX con Murastella Impresa Edile"

CTA: Richiedi subito una consulenza gratui
Riferimenti:
3415827063
info@murastella-example.it
murastella-example.it
seguici su Facebook

Target Market(s)

Man & Woman 26+, medium income, house owners, soccer fans. The board will be showed during soccer games,

Industry/Entity Type

Construction Company

Colors
ec1f27
eaf1f7
f3f1f8
cedeed

Requirements
Must have
• Murastella Logo.
• Charater text very big, it must be readable from the other side of a soccer filed.
• Text and services are the center of the requested design. Images are not necessary.
Nice to have
• It would be nice if play with differt background colors (almost grey and red, but you could use also other colors, like light grey for example!). We'd like not only "rectangular lines" to divide the spaces.

```html
<!DOCTYPE html>
<html lang="it">
<head>
<meta charset="utf-8">
<title>Murastella Impresa Edile – Banner bordocampo</title>
<link rel="stylesheet" href="https://fonts.googleapis.com/css2?family=Anton&display=swap">
<style>
  :root {
    --brand-red: #e3131b;
    --band-grey: #5c5c5c;
    --text-grey: #4a4a4a;
    --white: #ffffff;
    --stage: #e4e8ec;
    --outline: #1a1a1a;
  }
  * { margin: 0; padding: 0; box-sizing: border-box; }
  html, body { width: 1200px; height: 927px; overflow: hidden; background: var(--stage); }
  .canvas { position: relative; width: 1200px; height: 927px; }
  .banner {
    position: absolute; left: 20px; top: 232px;
    width: 1160px; height: 463px;
    background: var(--white);
    overflow: hidden;
    font-family: "Anton", "Oswald", sans-serif;
    box-shadow: 0 6px 18px rgba(0,0,0,.18);
  }
  .headline {
    position: absolute; left: 18px; top: 30px;
    color: var(--brand-red); font-size: 68px; font-weight: 400; line-height: 1; letter-spacing: .3px;
    white-space: nowrap;
  }
  .band {
    position: absolute; left: 0; width: 760px; height: 66px;
    color: var(--white); font-size: 38px; line-height: 66px;
    padding-left: 18px; white-space: nowrap;
  }
  .band--services { top: 152px; background: var(--brand-red); }
  .band--relax { top: 218px; background: var(--band-grey); }
  .contact {
    position: absolute; display: flex; align-items: center; gap: 8px;
    color: var(--text-grey); white-space: nowrap; line-height: 1;
  }
  .contact svg { flex: none; }
  .contact--phone  { left: 18px;  top: 306px; font-size: 56px; }
  .contact--mail   { left: 18px;  top: 390px; font-size: 28px; }
  .contact--web    { left: 424px; top: 318px; font-size: 28px; }
  .contact--social { left: 424px; top: 386px; font-size: 38px; }
  .visual { position: absolute; inset: 0; }
  .brand-mark {
    position: absolute; left: 860px; top: 58px;
    display: flex; align-items: center; gap: 12px;
    color: var(--brand-red); font-size: 50px; line-height: 1;
  }
  .brand-mark .square { width: 34px; height: 34px; background: var(--brand-red); }
</style>
</head>
<body>
<div class="canvas">
  <div class="banner">
    <h1 class="headline">Murastella Impresa Edile</h1>
    <div class="band band--services">Ristrutturazioni d'Interni ed Esterni</div>
    <div class="band band--relax">TOTAL RELAX con Murastella Impresa Edile</div>

    <div class="contact contact--phone">
      <svg width="48" height="48" viewBox="0 0 48 48" aria-hidden="true">
        <circle cx="24" cy="24" r="23" fill="var(--brand-red)"/>
        <path d="M17 12c2 0 3 1 4 5l-2 3c1 3 4 7 7 8l3-2c4 1 5 2 5 4s-3 5-6 5c-9-1-17-10-17-18 0-3 3-5 6-5z" fill="#fff"/>
      </svg>
      <span>3415827063</span>
    </div>
    <div class="contact contact--mail">
      <svg width="42" height="42" viewBox="0 0 46 46" aria-hidden="true">
        <circle cx="23" cy="23" r="21" fill="none" stroke="var(--brand-red)" stroke-width="3"/>
        <rect x="11" y="15" width="24" height="16" fill="none" stroke="var(--brand-red)" stroke-width="2.5"/>
        <path d="M11 15l12 10 12-10M11 31l9-8M35 31l-9-8" fill="none" stroke="var(--brand-red)" stroke-width="2.5"/>
      </svg>
      <span>info@murastella-example.it</span>
    </div>
    <div class="contact contact--web">
      <svg width="40" height="40" viewBox="0 0 44 44" aria-hidden="true">
        <g fill="none" stroke="var(--brand-red)" stroke-width="2.5">
          <circle cx="22" cy="22" r="19"/>
          <ellipse cx="22" cy="22" rx="8" ry="19"/>
          <path d="M3 22h38M6 12h32M6 32h32M22 3v38"/>
        </g>
      </svg>
      <span>murastella-example.it</span>
    </div>
    <div class="contact contact--social">
      <svg width="42" height="42" viewBox="0 0 44 44" aria-hidden="true">
        <circle cx="22" cy="22" r="21" fill="var(--brand-red)"/>
      </svg>
      <span>seguici su</span>
    </div>

    <svg class="visual" width="1160" height="463" viewBox="0 0 1160 463">
      <defs>
        <clipPath id="disc"><circle cx="1058" cy="231" r="325"/></clipPath>
        <linearGradient id="room-a" x1="0" y1="0" x2="1" y2="1">
          <stop offset="0" stop-color="#f2f1ee"/><stop offset="1" stop-color="#c9b79a"/>
        </linearGradient>
        <linearGradient id="room-b" x1="0" y1="0" x2="1" y2="1">
          <stop offset="0" stop-color="#ece9e4"/><stop offset="1" stop-color="#d2a36a"/>
        </linearGradient>
        <linearGradient id="room-c" x1="0" y1="0" x2="0" y2="1">
          <stop offset="0" stop-color="#d9d3e6"/><stop offset="1" stop-color="#b9bcc4"/>
        </linearGradient>
      </defs>
      <g clip-path="url(#disc)">
        <rect x="700" y="0" width="460" height="463" fill="var(--white)"/>
        <rect x="700" y="168" width="460" height="295" fill="var(--brand-red)"/>
        <rect x="700" y="171" width="291" height="134" fill="url(#room-a)" role="img" aria-label="Rendering di un soggiorno ristrutturato con libreria"/>
        <rect x="700" y="309" width="291" height="154" fill="url(#room-b)" role="img" aria-label="Rendering di una zona giorno con cucina e parquet"/>
        <rect x="995" y="171" width="165" height="292" fill="url(#room-c)" role="img" aria-label="Interno moderno con luci soffuse e piante"/>
      </g>
      <circle cx="1058" cy="231" r="325" fill="none" stroke="var(--outline)" stroke-width="3"/>
    </svg>

    <div class="brand-mark">
      <span class="square"></span>
      <span>MURASTELLA</span>
    </div>
  </div>
</div>
</body>
</html>
```